pathology learning flashcard template graphic design .

Creative designs for 2 sides of the flashcards to include colorful sectioning and font sizes that will make it easy to use in studying.

```html
<!DOCTYPE html>
<html lang="en">
<head>
<meta charset="utf-8">
<title>Pathology Flashcard – Case 0001</title>
<link rel="stylesheet" href="https://fonts.googleapis.com/css2?family=PT+Sans:ital,wght@0,400;0,700;1,400;1,700&family=PT+Sans+Narrow:wght@700&display=swap">
<style>
:root{
  --blue:#0b67b2;
  --pale:#d5eaf9;
  --ink:#111;
  --white:#fff;
  --grey:#8a8a8a;
}
*{box-sizing:border-box;margin:0;padding:0}
html,body{width:863px;height:1200px;overflow:hidden;background:var(--white)}
body{position:relative;font-family:"PT Sans",sans-serif;color:var(--ink)}
.sheet{position:absolute;left:0;width:863px;border:1px solid #555}
.sheet--front{top:0;height:592px}
.sheet--back{top:604px;height:596px}

/* front */
.front-card{position:absolute;left:21px;top:20px;width:822px;height:552px;border:3.5px solid var(--ink);border-radius:34px;overflow:hidden;background:var(--white)}
.front-card__question-panel{position:absolute;left:345px;top:0;right:0;bottom:0;background:var(--pale)}
.system-title{position:absolute;left:20px;top:20px;font-family:"PT Sans Narrow",sans-serif;font-weight:700;font-size:39px;letter-spacing:.2px;color:var(--blue);line-height:1}
.organ-art{position:absolute;left:78px;top:68px;width:194px;height:194px;border-radius:50%;border:3px solid var(--blue);background:radial-gradient(circle at 55% 45%,#f4f4f4 0 38%,var(--pale) 40%)}
.case-band{position:absolute;left:4px;top:282px;width:341px;height:46px;background:var(--pale);font-weight:700;font-style:italic;font-size:23.5px;line-height:46px;padding-left:17px}
.sex-icon{position:absolute;left:33px;top:388px;width:52px;height:52px}
.patient-art{position:absolute;left:91px;top:336px;width:168px;height:168px;border-radius:50%;background:linear-gradient(180deg,var(--pale) 0 55%,#b9c3cb 55% 100%)}
.patient-age{position:absolute;left:0;width:345px;top:508px;text-align:center;font-family:"PT Sans Narrow",sans-serif;font-weight:700;font-size:23px}
.question{position:absolute;left:362px;top:17px;width:441px;font-size:21.6px;line-height:26.3px;text-align:justify}
.options{position:absolute;left:362px;top:416px;list-style:none;font-size:22px;line-height:27.5px}

/* back */
.back-card{position:absolute;left:21px;top:21px;width:822px;height:548px;border:3.5px solid var(--blue);border-radius:34px;overflow:hidden;background:var(--white)}
.disease-title{position:absolute;left:18px;top:18px;font-family:"PT Sans Narrow",sans-serif;font-weight:700;font-style:italic;font-size:38px;color:var(--blue);line-height:1}
.info-col{position:absolute;top:61px;width:380px;font-size:16.4px;line-height:19.1px;text-align:justify}
.info-col--left{left:16px}
.info-col--right{left:422px;top:80px}
.info-block{margin-bottom:19px}
.info-block h3{font-size:16.4px;font-weight:700;font-style:italic}
.answer-panel{position:absolute;left:0;right:0;top:357px;bottom:0;background:var(--pale);padding:14px 16px 0 16px}
.answer-panel h3{font-size:16.4px;font-weight:700;font-style:italic;line-height:19px}
.answer-panel p{font-size:16.4px;font-style:italic;line-height:19.1px;text-align:justify}
.sources{position:absolute;left:16px;top:133px;font-size:12.6px}
.card-number{position:absolute;right:-4px;bottom:-4px;width:70px;height:70px;border-radius:50%;border:3.5px solid var(--blue);background:var(--white);font-weight:700;font-size:40px;text-align:center;line-height:62px}
</style>
</head>
<body>

<section class="sheet sheet--front">
  <div class="front-card">
    <div class="front-card__question-panel"></div>
    <h1 class="system-title">GASTROINTESTINAL</h1>
    <div class="organ-art" role="img" aria-label="Illustration of a stomach filled with microbes"></div>
    <div class="case-band">PATHOLOGY CASE ID 0001</div>
    <svg class="sex-icon" viewBox="0 0 52 52" aria-label="Male">
      <circle cx="20" cy="32" r="15" fill="none" stroke="#111" stroke-width="4.5"/>
      <path d="M31 21 L47 5 M33 5 H47 V19" fill="none" stroke="#111" stroke-width="4.5"/>
    </svg>
    <div class="patient-art" role="img" aria-label="Illustrated patient avatar"></div>
    <p class="patient-age">Age: 50 years</p>
    <p class="question">50-year-old woman comes to the clinic because she has difficulty swallowing for the past few months. She says symptoms have been worsening. She also complains of cough, <em>mostly at night and in fear of choking, has stopped eating many foods,</em> losing about 12 lbs in the past 3 months. Past medical history is unremarkable. Vital signs are normal and physical exam is unremarkable. Chest x-ray with demonstrates an <em>air-fluid level, while manometry shows absent relaxation of the</em> lower esophageal sphincter during swallowing. What is the most likely diagnosis?</p>
    <ol class="options">
      <li>A) GERD</li>
      <li>B) Barret Esophagus</li>
      <li>C) Achalasia</li>
      <li><em>D) Eosinophilic esophagitis</em></li>
    </ol>
  </div>
</section>

<section class="sheet sheet--back">
  <div class="back-card">
    <h2 class="disease-title">Achalasia</h2>
    <div class="info-col info-col--left">
      <div class="info-block"><h3>Definition:</h3><p><em>Motility disorder where esophageal relaxation is impaired in the lower esophageal</em> sphincter (LES).</p></div>
      <div class="info-block"><h3>Etiology/Pathology:</h3><p><em>Destruction of inhibitory neurons in the Auerbach plexus.</em> Loss of peristalsis in the lower esophageal sphincter (lower two thirds of the esophagus).</p></div>
      <div class="info-block"><h3>P/E and Symptoms:</h3><p>Dysphagia that is progressive, regurgitation, weight-loss, dry cough, chest pain, GERD, esophageal perforation, squamous cell carcinoma, aspiration pneumonia.</p></div>
    </div>
    <div class="info-col info-col--right">
      <div class="info-block"><p><em>Barium swallow will show ‘bird’s beak’ and esophageal dilation. Manometry will present with increased resting lower esophageal</em> sphincter pressure. Endoscopy will usually present with normal <em>mucosa and LES dilation, and in some cases residual material such as undigested food particles may be present.</em></p></div>
      <div class="info-block"><h3>Rx:</h3><p><em>First line of treatment are nitrates, calcium channel blockers, and Botulinum toxin injection in the LES. Long term management options include esophageal dilation with pneumatic balloon and myotomy.</em></p></div>
    </div>
    <div class="answer-panel">
      <h3>C-Achalasia</h3>
      <p>Symptoms and studies suggestive of achalasia. Patient’s manometry presents with no relaxation of the lower esophageal sphincter during swallowing. Patient also complains of dysphagia and is unable to swallow properly, leading to weight loss. Patient has no past infection or inflammation, ruling out eosinophilic esophagitis. Patient does not have GERD, eliminating the possibility of Barrett esophagus, in which at least 5 years of acid reflux are beforehand to develop columnar metaplasia.</p>
      <p class="sources">Sources: Hollis Drug Guide; Marrow Pocket Pharmacopoeia; Dosagenotes.net; Clinibase.net</p>
    </div>
    <div class="card-number">1</div>
  </div>
</section>

</body>
</html>
```